Layout für Werbefahnen gesucht
Zielgruppe
Unsere Frühstückpension befindet sich in Jois am Neusiedlersee mit direktem Rebenhangblick. Wir haben auch ein Weingut was unsere Gäste sehr schätzen.
Unsere Zielgruppe sind Urlaubsgäste mit höheren Ansprüchen sowie Weinbegeistere , Naturliebhaber, Radfahrer und Seeliebhaber (Neusiedlersee) unser Haus wurde mit sehr hochwertigen Materialien ausgestattet.
Aufgabenstellung
3 STK Werbefahnen ( Fahnenmast stehen schon siehe Beilage Bild) Maße: Format 1000x4000 mm
Unser Logo sollte auf den Fahnen vorhanden sein, man soll erkennen - dass man hier Urlaub verbringen kann und Wein verkosten (genießen) oder auch kaufen kann.
Gerne mit netten kurzen Sprüchen oder Wortspielen (Urlaub mit Rebenhangblick oder so?.
Naturverbunden mit liebe zum Wein, die Farben sollten unserem Logo angepasst werden eher naturverbunden braun oder grün, 1 Fahne sollte nur für den Wein gestaltet werden und die anderen beiden für unser Gästehaus.

```html
<!DOCTYPE html>
<html lang="de">
<head>
<meta charset="utf-8">
<title>Gut Rebenhang – Werbefahnen</title>
<link rel="stylesheet" href="https://fonts.googleapis.com/css2?family=EB+Garamond:wght@400&family=Libre+Baskerville:wght@700&display=swap">
<style>
  :root {
    --page: #ffffff;
    --sand: #dfc9b8;
    --vine-green: #8a9a3e;
    --lake-blue: #8cc3e5;
    --cream: #efece7;
    --ink: #3a3a3a;
    --earth-brown: #6e3c1c;
    --light-text: #f4f1ea;
  }
  html, body {
    margin: 0;
    padding: 0;
    width: 1116px;
    height: 1200px;
    overflow: hidden;
    background: var(--page);
  }
  .canvas {
    position: relative;
    width: 1116px;
    height: 1200px;
  }
  .banner {
    position: absolute;
    top: 42px;
    width: 283px;
    height: 1133px;
    overflow: hidden;
  }
  .banner--wine { left: 73px; }
  .banner--nature { left: 430px; }
  .banner--stay { left: 783px; }
  .banner__shapes {
    position: absolute;
    inset: 0;
    display: block;
  }
  .banner__title {
    position: absolute;
    top: 80px;
    left: 0;
    width: 100%;
    margin: 0;
    text-align: center;
    font-family: "EB Garamond", Georgia, serif;
    font-weight: 400;
    font-size: 66px;
    letter-spacing: 2px;
    line-height: 1;
    white-space: nowrap;
  }
  .banner--wine .banner__title { color: var(--ink); }
  .banner--nature .banner__title { color: var(--light-text); }
  .banner--stay .banner__title { color: var(--lake-blue); }
  .brand-name {
    position: absolute;
    top: 722px;
    left: 0;
    width: 100%;
    margin: 0;
    text-align: center;
    font-family: "Libre Baskerville", Georgia, serif;
    font-weight: 700;
    font-size: 23px;
    letter-spacing: 1px;
    color: var(--earth-brown);
    white-space: nowrap;
  }
  .slogan {
    position: absolute;
    top: 934px;
    left: 0;
    width: 100%;
    margin: 0;
    padding: 0;
    list-style: none;
    text-align: center;
    font-family: "Libre Baskerville", Georgia, serif;
    font-weight: 700;
    font-size: 18px;
    letter-spacing: 1.5px;
    line-height: 48px;
    white-space: nowrap;
  }
  .banner--wine .slogan { color: var(--ink); }
  .banner--nature .slogan { color: var(--light-text); top: 940px; }
  .banner--stay .slogan { color: var(--ink); top: 939px; }
</style>
</head>
<body>
<main class="canvas">

  <section class="banner banner--wine">
    <svg class="banner__shapes" viewBox="0 0 283 1133" width="283" height="1133">
      <defs>
        <linearGradient id="wine-scene" x1="0" y1="0" x2="0" y2="1">
          <stop offset="0" stop-color="#8cc3e5"/>
          <stop offset="0.55" stop-color="#b9d8ec"/>
          <stop offset="0.74" stop-color="#dfe8ec"/>
          <stop offset="0.8" stop-color="#6e8a4a"/>
          <stop offset="1" stop-color="#4f7338"/>
        </linearGradient>
      </defs>
      <rect class="zone-top" width="283" height="600" fill="var(--sand)"/>
      <path role="img" aria-label="Weinflasche vor Weinbergen mit Blick auf den See" fill="url(#wine-scene)"
            d="M0,278 C35,256 85,252 120,262 C160,275 190,314 228,312 C255,310 270,290 283,278 L283,596 L0,596 Z"/>
      <rect class="zone-logo" y="596" width="283" height="537" fill="var(--cream)"/>
      <path class="zone-bottom" fill="var(--sand)"
            d="M0,888 C30,866 80,860 115,875 C150,890 185,920 220,916 C250,912 270,900 283,898 L283,1133 L0,1133 Z"/>
    </svg>
    <h2 class="banner__title">genießen</h2>
    <p class="brand-name">GUT REBENHANG</p>
    <ul class="slogan">
      <li>VERKOSTUNG</li>
      <li>UND</li>
      <li>VERKAUF</li>
    </ul>
  </section>

  <section class="banner banner--nature">
    <svg class="banner__shapes" viewBox="0 0 283 1133" width="283" height="1133">
      <defs>
        <linearGradient id="nature-scene" x1="0" y1="0" x2="0" y2="1">
          <stop offset="0" stop-color="#8cc3e5"/>
          <stop offset="0.45" stop-color="#a9d0ea"/>
          <stop offset="0.6" stop-color="#e4eef3"/>
          <stop offset="0.72" stop-color="#9cc6e0"/>
          <stop offset="0.78" stop-color="#5f7d3c"/>
          <stop offset="0.88" stop-color="#a9bd3e"/>
          <stop offset="1" stop-color="#c4cf45"/>
        </linearGradient>
      </defs>
      <rect class="zone-top" width="283" height="600" fill="var(--vine-green)"/>
      <path role="img" aria-label="Weite Felder unter Himmel mit Wolken" fill="url(#nature-scene)"
            d="M0,278 C35,256 85,252 120,262 C160,275 190,314 228,312 C255,310 270,290 283,278 L283,596 L0,596 Z"/>
      <rect class="zone-logo" y="596" width="283" height="537" fill="var(--cream)"/>
      <path class="zone-bottom" fill="var(--vine-green)"
            d="M0,888 C30,866 80,860 115,875 C150,890 185,920 220,916 C250,912 270,900 283,898 L283,1133 L0,1133 Z"/>
    </svg>
    <h2 class="banner__title">erleben</h2>
    <p class="brand-name">GUT REBENHANG</p>
    <ul class="slogan">
      <li>RADFAHREN</li>
      <li>WANDERN</li>
      <li>SEE-AKTIVITÄTEN</li>
    </ul>
  </section>

  <section class="banner banner--stay">
    <svg class="banner__shapes" viewBox="0 0 283 1133" width="283" height="1133">
      <defs>
        <linearGradient id="stay-scene" x1="0" y1="0" x2="0" y2="1">
          <stop offset="0" stop-color="#8cc3e5"/>
          <stop offset="0.4" stop-color="#8cc3e5"/>
          <stop offset="0.5" stop-color="#3f94d2"/>
          <stop offset="0.62" stop-color="#cfe6f4"/>
          <stop offset="0.72" stop-color="#5f8fa8"/>
          <stop offset="0.8" stop-color="#2e6e9c"/>
          <stop offset="1" stop-color="#1d4f78"/>
        </linearGradient>
      </defs>
      <rect class="zone-top" width="283" height="600" fill="var(--cream)"/>
      <path role="img" aria-label="Hafen am See mit Booten, Pfählen und Schilf" fill="url(#stay-scene)"
            d="M0,278 C35,256 85,252 120,262 C160,275 190,314 228,312 C255,310 270,290 283,278 L283,596 L0,596 Z"/>
      <rect class="zone-logo" y="596" width="283" height="537" fill="var(--cream)"/>
      <path class="zone-bottom" fill="var(--lake-blue)"
            d="M0,888 C30,866 80,860 115,875 C150,890 185,920 220,916 C250,912 270,900 283,898 L283,1133 L0,1133 Z"/>
    </svg>
    <h2 class="banner__title">erholen</h2>
    <p class="brand-name">GUT REBENHANG</p>
    <ul class="slogan">
      <li>URLAUB</li>
      <li>MIT</li>
      <li>REBENHANGBLICK</li>
    </ul>
  </section>

</main>
</body>
</html>
```